Redesign of a growing event production company in atlanta!

www.qvrstaging.com - it's Plonko.com site and I'd like to keep it within PLONKO if possible.
We purchased a new logo and we are looking for a redesign.
We specialize in many different aspects of the event production industry and we want our page to be better segmented, with separation between the audio video lighting and wedding services offered.
We also want this cleaned up, showcasing client feedback and highlighted photos. Our industry is very visual and we want some of our work showcased as well as area for event videos.
We want the ability to add new photos and videos as well as links to our blog. If we can incorporate our blog into the site, that would be great as well.
Attached is the new logo, we are going to have it animated and placed on the site as well. We love the color spectrum of light and the significance to event production. We would like the page to incorporate that.

Target Market(s)

Women are the main purchasees of our services. brides between 20 - 40, and then corporate event planners...we have a high end market. We are marketing to the people who plan galas and society socials.

Industry/Entity Type

It Company

Number of Pages Required

5+ page

Font styles to use
Sans Serif
Script

Requirements
Must have
• incorporate the same content I currently have on my site.
• A clear but fluid separation between our event production services (Audio Visual) and the wedding services we offer. We MUST also be able to clearly show what we do. We are a one stop show and we want to convey that.
Nice to have
• Color palette based off logo attached

```html
<!DOCTYPE html>
<html lang="en">
<head>
<meta charset="utf-8">
<title>Lumora Events</title>
<link rel="stylesheet" href="https://fonts.googleapis.com/css2?family=Lato:ital,wght@0,400;0,700;1,400&family=Roboto+Condensed:wght@400&family=Roboto+Slab:wght@400&family=Quicksand:wght@400&display=swap">
<style>
:root{
  --plum:#7a1450;
  --plum-dark:#5e0d3c;
  --magenta:#b0186e;
  --pink:#e8409a;
  --ink:#111;
  --night:#0c0f24;
  --night-2:#1c1f3d;
  --gold:#e6c35a;
  --text:#333;
  --muted:#777;
  --white:#fff;
}
*{margin:0;padding:0;box-sizing:border-box}
html,body{width:1200px;height:2695px;overflow:hidden;background:var(--white)}
body{position:relative;font-family:'Lato',sans-serif;color:var(--text)}
.abs{position:absolute}
.top-band{left:0;top:0;width:1200px;height:66px;background:var(--plum)}
.header{left:0;top:62px;width:1200px;height:108px;background:var(--ink)}
.social{display:flex;gap:8px}
.social span{width:32px;height:32px;border-radius:50%;background:#bbb;border:2px solid #eee;display:block}
.social span:first-child{background:#3aa6e0}
.brand-mark{left:180px;top:8px;width:108px;height:108px;border-radius:50%;background:var(--ink);border:4px solid #ddd}
.brand-name{left:98px;top:112px;font-family:'Lato',sans-serif;font-weight:700;font-size:34px;letter-spacing:2px;color:var(--white)}
.brand-sub{left:100px;top:150px;font-size:11px;letter-spacing:4px;color:#bbb}
.phone{left:925px;top:76px;color:var(--gold);font-size:22px;display:flex;align-items:center;gap:10px}
.nav{top:126px;font-family:'Roboto Condensed',sans-serif;font-size:16px;color:var(--white);display:flex;gap:0}
.nav a{position:absolute;color:var(--white);text-decoration:none;white-space:nowrap}
.nav a.active{color:var(--gold);border-bottom:2px solid var(--gold);padding-bottom:6px}
.hero{left:0;top:170px;width:1200px;height:590px}
.hero-caption{left:300px;top:488px;width:570px;height:44px;background:rgba(0,0,0,.35);color:var(--white);font-family:'Roboto Slab',serif;font-size:30px;text-align:center;line-height:44px;letter-spacing:1px}
.hero-arrow{width:32px;height:32px;border-radius:50%;background:#222;top:462px}
.welcome-title{left:0;top:742px;width:1200px;text-align:center;font-family:'Roboto Slab',serif;font-size:36px;color:#111}
.welcome-lead{left:0;top:796px;width:1200px;text-align:center;font-style:italic;font-size:15px;color:#222}
.welcome-body{left:300px;top:830px;width:600px;text-align:center;font-size:13px;line-height:22px;color:#444}
.service-icon{width:156px;height:156px;border-radius:50%;border:4px solid var(--magenta);background:radial-gradient(circle,#2a1a3a,#0a0a12)}
.service-title{font-family:'Roboto Slab',serif;font-size:26px;color:var(--magenta)}
.service-text{width:270px;font-size:16px;line-height:24px;color:#222}
.service-more{font-size:13px;color:var(--muted)}
.showcase-title{left:95px;top:1232px;font-family:'Roboto Slab',serif;font-size:28px;color:var(--white);letter-spacing:1px}
.tile{width:244px;height:185px;overflow:hidden}
.tile .photo{width:100%;height:100%}
.tile .cap{position:absolute;left:0;bottom:0;width:100%;height:36px;background:rgba(0,0,0,.7);color:var(--white);font-size:13px;line-height:36px;padding-left:12px}
.tile .zoom{position:absolute;right:0;bottom:0;width:36px;height:36px;background:rgba(60,60,60,.9)}
.chev{font-size:44px;color:var(--pink);font-family:'Lato',sans-serif}
.testi-title{left:0;top:1875px;width:1200px;text-align:center;font-family:'Quicksand',sans-serif;font-size:36px;color:#111}
.portrait{width:108px;height:108px;border-radius:50%;border:4px solid #444}
.quote{width:310px;font-size:13px;line-height:22px;color:#222}
.quote-name{font-size:15px;font-weight:700;color:var(--plum)}
.footer-nav a{position:absolute;top:2224px;font-family:'Roboto Condensed',sans-serif;font-size:16px;color:var(--white);text-decoration:none}
.footer-nav a.active{color:var(--gold)}
.f-head{top:2300px;font-family:'Quicksand',sans-serif;font-size:26px;color:var(--white)}
.f-text{font-size:13px;line-height:21px;color:#ddd}
.readmore{left:128px;top:2536px;border:1px solid var(--pink);color:var(--pink);font-size:11px;padding:1px 6px}
.thumb{width:104px;height:80px}
.bottom-band{left:0;top:2582px;width:1200px;height:113px;background:var(--plum)}
.copyright{left:128px;top:2645px;font-size:13px;color:var(--white)}
</style>
</head>
<body>

<div class="abs top-band"></div>
<div class="abs social" style="left:822px;top:12px"><span></span><span></span><span></span><span></span><span></span><span></span><span></span></div>

<header class="abs header"></header>
<div class="abs brand-mark"></div>
<div class="abs brand-name">LUMORA EVENTS</div>
<div class="abs brand-sub">LUMORA EVENT PRODUCTION</div>
<div class="abs phone">
  <svg width="26" height="26" viewBox="0 0 26 26"><circle cx="13" cy="13" r="12" fill="none" stroke="#fff" stroke-width="2"/><path d="M9 7l3 3-1.5 2a8 8 0 0 0 3.5 3.5l2-1.5 3 3-2 2c-5 0-10-5-10-10z" fill="#fff"/></svg>
  888 555 0147
</div>
<nav class="abs nav" style="left:0;width:1200px">
  <a class="active" style="left:447px">HOME</a>
  <a style="left:524px">ABOUT US</a>
  <a style="left:630px">OUR SERVICES</a>
  <a style="left:765px">EVENTS</a>
  <a style="left:852px">GALLERY</a>
  <a style="left:950px">BLOG</a>
  <a style="left:1024px">CONTACT US</a>
</nav>

<svg class="abs hero" viewBox="0 0 1200 590" role="img" aria-label="Wedding party celebrating with the bride and groom kissing under a floral arch">
  <defs><linearGradient id="heroFill" x1="0" y1="0" x2="1" y2="1"><stop offset="0" stop-color="#e8e1d2"/><stop offset=".5" stop-color="#9c9590"/><stop offset="1" stop-color="#3a3533"/></linearGradient></defs>
  <polygon points="0,0 1200,0 1200,460 0,590" fill="url(#heroFill)"/>
</svg>
<div class="abs hero-caption">EVERY EVENTS SHOULD BE PERFECT</div>
<div class="abs hero-arrow" style="left:30px"><svg width="32" height="32"><path d="M19 9l-7 7 7 7" stroke="#fff" stroke-width="2.5" fill="none"/></svg></div>
<div class="abs hero-arrow" style="left:1146px"><svg width="32" height="32"><path d="M13 9l7 7-7 7" stroke="#fff" stroke-width="2.5" fill="none"/></svg></div>

<h1 class="abs welcome-title">WELCOME TO LUMORA EVENTS</h1>
<p class="abs welcome-lead">Lorem ipsum dolor sit amet, consectetur adipiscing eli Vestibulum efficitur pellentesque mi, ut vestibulum mauris sagittis at.</p>
<p class="abs welcome-body">Aliquam vitae magna aliquet, molestie est eget, ultricies arcu. Nunc non luctus turpis, et sollicitudin sem. In at vehicula tellus. Nulla vel eleifend nulla, quis ultrices metus. Nunc finibus nisi ac congue tempor. Nulla elementum, leo non vehicula lacinia, velit .</p>

<div class="abs service-icon" style="left:115px;top:924px" role="img" aria-label="Illustration of a DJ at a mixing desk"></div>
<h2 class="abs service-title" style="left:303px;top:938px">EVENT SERVICES</h2>
<p class="abs service-text" style="left:303px;top:976px">Aliquam vitae magna aliquet, molestie est eget, ultricies arcu. Nunc non luctus turpis, et sollicitudin sem. In at vehicula tellus. Nulla vel eleifend nulla.</p>
<span class="abs service-more" style="left:305px;top:1082px">MORE INFO</span>

<div class="abs service-icon" style="left:632px;top:924px" role="img" aria-label="Illustration of a bride and groom"></div>
<h2 class="abs service-title" style="left:820px;top:938px">WEDDING SERVICES</h2>
<p class="abs service-text" style="left:820px;top:976px">Aliquam vitae magna aliquet, molestie est eget, ultricies arcu. Nunc non luctus turpis, et sollicitudin sem. In at vehicula tellus. Nulla vel eleifend nulla.</p>
<span class="abs service-more" style="left:822px;top:1082px">MORE INFO</span>

<svg class="abs" style="left:0;top:1110px" width="1200" height="740"><polygon points="0,95 1200,0 1200,735 0,660" fill="var(--plum)"/></svg>
<h2 class="abs showcase-title">OUR SHOWCASE</h2>
<span class="abs chev" style="left:40px;top:1470px">&#8249;</span>
<span class="abs chev" style="left:1134px;top:1470px">&#8250;</span>

<div class="abs tile" style="left:93px;top:1307px"><div class="photo" role="img" aria-label="Tented reception with golden drapery" style="background:linear-gradient(#c89a40,#5a3a20)"></div><div class="cap">Lorem ipsum dolor sit amet</div><div class="zoom"></div></div>
<div class="abs tile" style="left:347px;top:1307px"><div class="photo" role="img" aria-label="Bridal party group outdoors" style="background:linear-gradient(#6a7468,#c9b8a8)"></div><div class="cap">Lorem ipsum dolor sit amet</div><div class="zoom"></div></div>
<div class="abs tile" style="left:606px;top:1307px"><div class="photo" role="img" aria-label="Red lanterns over a dessert table" style="background:linear-gradient(#c02030,#5a1018)"></div><div class="cap">Lorem ipsum dolor sit amet</div><div class="zoom"></div></div>
<div class="abs tile" style="left:863px;top:1307px"><div class="photo" role="img" aria-label="Flower girls in white dresses" style="background:linear-gradient(#b08060,#e8e0d8)"></div><div class="cap">Lorem ipsum dolor sit amet</div><div class="zoom"></div></div>
<div class="abs tile" style="left:93px;top:1522px"><div class="photo" role="img" aria-label="Ballroom with purple uplighting" style="background:linear-gradient(#d0a030,#6a3aa0)"></div><div class="cap">Lorem ipsum dolor sit amet</div><div class="zoom"></div></div>
<div class="abs tile" style="left:347px;top:1522px"><div class="photo" role="img" aria-label="Stage lighting rig in violet light" style="background:linear-gradient(#8a30d0,#3a1070)"></div><div class="cap">Lorem ipsum dolor sit amet</div><div class="zoom"></div></div>
<div class="abs tile" style="left:606px;top:1522px"><div class="photo" role="img" aria-label="Banquet hall in pink lighting" style="background:linear-gradient(#c03890,#3a1030)"></div><div class="cap">Lorem ipsum dolor sit amet</div><div class="zoom"></div></div>
<div class="abs tile" style="left:863px;top:1522px"><div class="photo" role="img" aria-label="Reception hall with green accent lights" style="background:linear-gradient(#6a9a50,#8a5a3a)"></div><div class="cap">Lorem ipsum dolor sit amet</div><div class="zoom"></div></div>

<div class="abs" style="left:572px;top:1772px;width:56px;height:56px;border-radius:50%;background:#fff;border:3px solid var(--plum)"></div>

<h2 class="abs testi-title">Client Testimonials</h2>
<svg class="abs" style="left:74px;top:1978px" width="20" height="30"><path d="M16 3L5 15l11 12" stroke="#aaa" stroke-width="3" fill="none"/></svg>
<svg class="abs" style="left:1096px;top:1978px" width="20" height="30"><path d="M4 3l11 12L4 27" stroke="#333" stroke-width="3" fill="none"/></svg>

<div class="abs portrait" style="left:111px;top:1938px;background:linear-gradient(#6a7a8a,#2a3a5a)" role="img" aria-label="Portrait of client Martin Hale"></div>
<p class="abs quote" style="left:228px;top:1956px">&#8220; Lorem ipsum dolor sit amet, consectetuer adipiscing elit, sed diam nonummy nibh euismod tincidunt ut laoreet dolore magna aliquam erat volutpat. Ut wisi enim ad minim veniam &#8221;</p>
<span class="abs quote-name" style="left:236px;top:2058px">Martin Hale</span>

<div class="abs portrait" style="left:611px;top:1938px;background:linear-gradient(#d8d0c8,#8a7a6a)" role="img" aria-label="Portrait of client Edith Rowe"></div>
<p class="abs quote" style="left:728px;top:1956px">&#8220; Lorem ipsum dolor sit amet, consectetuer adipiscing elit, sed diam nonummy nibh euismod tincidunt ut laoreet dolore magna aliquam erat volutpat. Ut wisi enim ad minim veniam &#8221;</p>
<span class="abs quote-name" style="left:734px;top:2058px">Edith Rowe</span>

<svg class="abs" style="left:0;top:2110px" width="1200" height="480"><defs><linearGradient id="night" x1="0" y1="0" x2="0" y2="1"><stop offset="0" stop-color="#1a1d3a"/><stop offset="1" stop-color="#080a1c"/></linearGradient></defs><polygon points="0,80 1200,0 1200,480 0,480" fill="url(#night)"/></svg>
<div class="abs" style="left:566px;top:2112px;width:68px;height:68px;border-radius:50%;background:var(--ink);border:3px solid #ccc"></div>

<nav class="footer-nav">
  <a class="active" style="left:165px">HOME</a>
  <a style="left:284px">ABOUT US</a>
  <a style="left:408px">OUR SERVICES</a>
  <a style="left:692px">EVENTS</a>
  <a style="left:802px">GALLERY</a>
  <a style="left:922px">BLOG</a>
  <a style="left:1016px">CONTACT US</a>
</nav>

<h3 class="abs f-head" style="left:128px">About Lumora Events</h3>
<p class="abs f-text" style="left:128px;top:2352px;width:240px">Lumora Event Production's team has diverse professional experience working in professional Entertainment, Catering, Audio/Video Production, Venue Management and Lighting Production. This seperates us from our competition, giving you the best event experience!</p>
<span class="abs readmore">Read More</span>

<h3 class="abs f-head" style="left:432px">Contact Information</h3>
<svg class="abs" style="left:440px;top:2360px" width="14" height="20"><path d="M7 0a7 7 0 0 1 7 7c0 5-7 13-7 13S0 12 0 7a7 7 0 0 1 7-7z" fill="#aaa"/><circle cx="7" cy="7" r="2.5" fill="#111"/></svg>
<p class="abs f-text" style="left:470px;top:2352px;width:170px"><b style="color:#fff">Lumora Events</b><br>Lorem ipsum dolor sit amet, consectetu adipiscing elit</p>
<svg class="abs" style="left:438px;top:2438px" width="18" height="18"><path d="M3 1l4 4-2 3a10 10 0 0 0 5 5l3-2 4 4-3 3C7 18 0 11 0 4z" fill="#aaa"/></svg>
<span class="abs" style="left:470px;top:2434px;font-size:18px;color:#fff">1-555-01234</span>
<svg class="abs" style="left:438px;top:2478px" width="20" height="14"><rect x="1" y="1" width="18" height="12" fill="none" stroke="#aaa" stroke-width="2"/><path d="M1 1l9 7 9-7" stroke="#aaa" stroke-width="2" fill="none"/></svg>
<span class="abs f-text" style="left:470px;top:2474px">hello@lumoraevents.com</span>

<h3 class="abs f-head" style="left:740px">Photo Gallery</h3>
<div class="abs thumb" style="left:695px;top:2340px;background:linear-gradient(#f0f0f0,#9a8aa0)" role="img" aria-label="Event photo"></div>
<div class="abs thumb" style="left:864px;top:2362px;background:linear-gradient(#3a5aa0,#1a1a3a)" role="img" aria-label="Conference stage photo"></div>
<div class="abs thumb" style="left:983px;top:2362px;background:linear-gradient(#c87040,#5a2a1a)" role="img" aria-label="Banquet hall photo"></div>
<div class="abs thumb" style="left:745px;top:2460px;background:linear-gradient(#7a8a50,#3a3a20)" role="img" aria-label="Reception photo"></div>
<div class="abs thumb" style="left:864px;top:2460px;background:linear-gradient(#2a2a3a,#6a6a7a)" role="img" aria-label="Corporate event photo"></div>
<div class="abs thumb" style="left:983px;top:2460px;background:linear-gradient(#d8c8b0,#7a6a5a)" role="img" aria-label="Wedding ceremony photo"></div>
<span class="abs" style="left:770px;top:2546px;font-size:11px;color:var(--pink)">More + +</span>

<div class="abs bottom-band"></div>
<p class="abs copyright">Copyright &copy; 2015 Lumora Events. All Rights Reserved.</p>
<div class="abs social" style="left:826px;top:2640px"><span></span><span></span><span></span><span></span><span></span><span></span><span></span></div>

</body>
</html>
```